Tickle Your Toes! Summer One Act Festival

I need a poster design for a summer festival of short comedy plays in San Francisco, all with a historical or intellectual theme! From Ancient Greece to the Russian Revolution to Cold War Politics to College Admissions! The target audience demographic is 20-30 year old San Francisco "hipster types" who will be attending a food truck festival. The festival performance dates are Friday evenings, July 22 to August 15! We would like a clever, antique looking design that conveys comedy and history. We would also like the names of the plays, all by the same author, Milo Fairbank, on the poster as well! The titles are:

Vexilla
Gin and Quibbles
The Endless Oboe Concerto
Quill Snap
Lighthouse Deliberations
Pigeons Hold a Vote

```html
<!DOCTYPE html>
<html lang="en">
<head>
<meta charset="utf-8">
<title>Tickle Your Toes! Summer One Act Festival</title>
<link href="https://fonts.googleapis.com/css2?family=Cinzel:wght@700&family=Old+Standard+TT:wght@700&family=Lato:wght@400&family=Berkshire+Swash&family=Big+Shoulders+Display:wght@200&family=Orbitron:wght@900&family=Lobster&family=Alfa+Slab+One&family=Poiret+One&family=Archivo+Black&family=Graduate&family=Kaushan+Script&display=swap" rel="stylesheet">
<style>
  :root {
    --ink: #111;
    --paper-top: #5f6e5c;
    --paper-mid: #c9d2a2;
    --paper-warm: #d7b27a;
    --paper-low: #8a6a3f;
    --rule: rgba(40,30,20,.45);
    --white: #fbf8f0;
    --gin-red: #b3182c;
    --amp-gold: #c99a1e;
    --quib-blue: #2a3fc2;
    --steel: #55646a;
    --maroon: #8a1a36;
    --slap-red: #d52b2b;
    --vote-yellow: #ecc93a;
    --script-red: #b8121e;
  }
  html, body { margin: 0; padding: 0; overflow: hidden; }
  body { width: 1042px; height: 1200px; background: #6b6a55; }

  .poster {
    position: relative;
    width: 1042px; height: 1200px;
    overflow: hidden;
    background:
      radial-gradient(ellipse 75% 65% at 50% 55%, rgba(255,250,215,.55), rgba(255,250,215,0) 70%),
      linear-gradient(180deg, var(--paper-top) 0%, #9aa88a 12%, var(--paper-mid) 30%, var(--paper-warm) 62%, #c09258 82%, var(--paper-low) 100%);
  }
  .frame {
    position: absolute;
    left: 43px; top: 36px; width: 955px; height: 1128px;
    border: 5px solid var(--ink);
    box-sizing: border-box;
  }
  .frame::after {
    content: ""; position: absolute; inset: 6px;
    border: 1.5px solid var(--ink);
  }
  .flourish {
    position: absolute; width: 56px; height: 56px;
    background: radial-gradient(circle at 35% 35%, rgba(17,17,17,.55), rgba(17,17,17,0) 70%);
  }
  .flourish.tl { left: 52px; top: 45px; }
  .flourish.tr { right: 52px; top: 45px; transform: scaleX(-1); }
  .flourish.bl { left: 52px; bottom: 45px; transform: scaleY(-1); }
  .flourish.br { right: 52px; bottom: 45px; transform: scale(-1,-1); }

  .masthead { position: absolute; left: 0; right: 0; top: 56px; text-align: center; color: var(--white); }
  .presenter { font: 400 17px "Lato", sans-serif; letter-spacing: .5px; }
  .festival-title {
    margin: 4px 0 0; font: 700 44px "Cinzel", serif; letter-spacing: 1px;
    text-shadow: 0 2px 3px rgba(0,0,0,.35);
  }
  .byline { font: 400 16px "Lato", sans-serif; margin-top: 2px; }

  .dates {
    position: absolute; left: 50px; right: 50px; top: 196px; height: 64px;
    border-top: 1px dashed var(--rule); border-bottom: 1px dashed var(--rule);
    display: flex; align-items: center; justify-content: center;
    font: 700 30px "Old Standard TT", serif; letter-spacing: 1.5px; color: var(--ink);
  }
  .dates sup { font-size: 16px; }

  .playbill {
    position: absolute; left: 50px; top: 262px; width: 942px; height: 890px;
    display: grid; grid-template-columns: 476px 466px; grid-template-rows: 300px 288px 302px;
  }
  .play {
    position: relative; display: flex; flex-direction: column;
    align-items: center; justify-content: center; text-align: center;
    border-bottom: 1px dashed var(--rule);
  }
  .play:nth-child(odd) { border-right: 1px dashed var(--rule); }
  .play:nth-last-child(-n+2) { border-bottom: none; }

  /* Gin & Quibbles */
  .gin { font-family: "Berkshire Swash", serif; line-height: .9; text-shadow: 2px 3px 3px rgba(0,0,0,.45); }
  .gin .w1 { font-size: 80px; color: var(--gin-red); margin-right: 90px; }
  .gin .amp { font-size: 58px; color: var(--amp-gold); }
  .gin .w2 { font-size: 76px; color: var(--quib-blue); margin-left: 60px; }

  /* Vexilla */
  .vexilla {
    font: 200 190px "Big Shoulders Display", sans-serif; letter-spacing: 4px;
    color: #cfd6d8; -webkit-text-stroke: 3px var(--steel);
    text-shadow: 4px 5px 6px rgba(0,0,0,.4); line-height: 1;
  }

  /* The Endless Oboe Concerto */
  .oboe { font-family: "Orbitron", sans-serif; font-weight: 900; color: var(--maroon); line-height: 1.05; }
  .oboe .l1 { font-size: 34px; }
  .oboe .l2 { font-size: 50px; letter-spacing: 2px; }
  .oboe .l3 { font-size: 60px; letter-spacing: 4px; }
  .oboe .l4 { font-size: 48px; }

  /* Quill Snap */
  .quill .w1 { font: 400 72px "Lobster", cursive; color: var(--ink); line-height: 1; }
  .quill .w2 {
    font: 400 98px "Alfa Slab One", serif; color: var(--slap-red); line-height: 1;
    text-shadow: 3px 3px 0 #fff, 7px 7px 0 #2a1a12; transform: skewX(-6deg);
  }

  /* Pigeons Hold a Vote */
  .pigeons { position: relative; width: 360px; height: 250px; }
  .pigeons .top { position: absolute; right: 20px; top: 30px; font: 400 34px "Archivo Black", sans-serif; color: var(--vote-yellow); text-shadow: 1px 2px 2px rgba(0,0,0,.4); }
  .pigeons .big { position: absolute; left: 40px; top: 52px; font: 400 112px "Poiret One", sans-serif; color: var(--ink); }
  .pigeons .a { position: absolute; left: 44px; top: 170px; font: 400 36px "Archivo Black", sans-serif; color: var(--vote-yellow); text-shadow: 1px 2px 2px rgba(0,0,0,.4); }
  .pigeons .end { position: absolute; left: 110px; top: 140px; font: 400 96px "Poiret One", sans-serif; color: var(--vote-yellow); text-shadow: 1px 2px 2px rgba(0,0,0,.35); }

  /* Lighthouse Deliberations */
  .lighthouse { line-height: 1; }
  .lighthouse .w1 { font: 400 86px "Graduate", serif; color: var(--white); letter-spacing: 4px; text-shadow: 2px 3px 3px rgba(0,0,0,.5); }
  .lighthouse .w2 { font: 400 48px "Graduate", serif; color: var(--white); letter-spacing: 3px; margin-top: 6px; text-shadow: 2px 3px 3px rgba(0,0,0,.5); }
  .lighthouse .w3 { font: 400 42px "Kaushan Script", cursive; color: var(--script-red); margin-top: 14px; text-shadow: 1px 1px 0 #fff, 2px 3px 2px rgba(0,0,0,.35); }
</style>
</head>
<body>
<main class="poster">
  <div class="frame"></div>
  <div class="flourish tl" role="img" aria-label="Corner scroll ornament"></div>
  <div class="flourish tr" role="img" aria-label="Corner scroll ornament"></div>
  <div class="flourish bl" role="img" aria-label="Corner scroll ornament"></div>
  <div class="flourish br" role="img" aria-label="Corner scroll ornament"></div>

  <header class="masthead">
    <div class="presenter">Summer One Act Festival presents ...</div>
    <h1 class="festival-title">Tickle Your Toes!</h1>
    <div class="byline">by Author, &nbsp;Milo Fairbank</div>
  </header>

  <div class="dates">FRIDAY EVENINGS, JULY 22<sup>ND</sup>&nbsp;-&nbsp;AUGUST 15<sup>TH</sup></div>

  <section class="playbill">
    <article class="play">
      <div class="gin"><div class="w1">Gin</div><div class="amp">&amp;</div><div class="w2">Quibbles</div></div>
    </article>
    <article class="play">
      <div class="vexilla">VEXILLA</div>
    </article>
    <article class="play">
      <div class="oboe"><div class="l1">THE</div><div class="l2">ENDLESS</div><div class="l3">OBOE</div><div class="l4">CONCERTO</div></div>
    </article>
    <article class="play">
      <div class="quill"><div class="w1">Quill</div><div class="w2">SNAP</div></div>
    </article>
    <article class="play">
      <div class="pigeons"><span class="top">PIGEONS</span><span class="big">Hold</span><span class="a">A</span><span class="end">vote</span></div>
    </article>
    <article class="play">
      <div class="lighthouse"><div class="w1">LIGHT</div><div class="w2">HOUSE</div><div class="w3">Deliberations</div></div>
    </article>
  </section>
</main>
</body>
</html>
```